Halvorn Minerals Web Design

Require a Web page design for an international mining and private investment company currently based in Dubai, UAE. I would like to view designs that incorporate our current corporate logo design aimed at communicating global business development/expansion across a diversity of commodities within the mining and investment sectors.

We are a global organisation with global experience and strategy with specific business development focus in Africa, Central and South America.

Target Market(s)

Mining industry, finance, fund raising, brokering, private equity and public stock exchanges.

Industry/Entity Type

Mining

Number of Pages Required

5+ page

Font styles to use
Sans Serif

Colors

Designer to choose colors to be used in the design.

Requirements
Must have
• Corporate logo, description of who we are, what we do, corporate mission, vision & strategy.
Nice to have
• Inclusion of images, photos, interactive maps/graphics and video.

```html
<!DOCTYPE html>
<html lang="en">
<head>
<meta charset="utf-8">
<title>Halvorn Minerals</title>
<link rel="stylesheet" href="https://fonts.googleapis.com/css2?family=Montserrat:wght@300;400;500;700;800&display=swap">
<style>
  :root {
    --cream: #fbfbef;
    --slate: #646464;
    --gold: #a88c4b;
    --gold-light: #e6bd71;
    --gold-mid: #c8a356;
    --ink: #3a3a3a;
    --white: #ffffff;
  }
  * { margin: 0; padding: 0; box-sizing: border-box; }
  html, body { width: 1119px; height: 1200px; overflow: hidden; }
  body {
    position: relative;
    background: var(--cream);
    font-family: "Montserrat", sans-serif;
    color: var(--ink);
  }
  .fringe-band {
    position: absolute; left: 0; top: 0; width: 1119px; height: 28px;
    background: linear-gradient(180deg, #d9c38e 0%, #e8dbb5 55%, rgba(251,251,239,0) 100%);
  }
  .site-header { position: absolute; left: 0; top: 28px; width: 1119px; height: 101px; }
  .brand {
    position: absolute; left: 77px; top: 34px;
    display: flex; align-items: center; gap: 10px;
    font-size: 22px; font-weight: 700; color: var(--gold); letter-spacing: 0.5px;
  }
  .brand-mark { width: 18px; height: 18px; background: var(--gold); }
  .main-nav a {
    position: absolute; top: 38px;
    font-size: 14px; letter-spacing: 3px; color: var(--ink); text-decoration: none;
  }
  .hero { position: absolute; left: 0; top: 129px; width: 1119px; height: 349px; }
  .hero svg { position: absolute; left: 0; top: 0; }
  .hero-title {
    position: absolute; left: 77px; top: 80px;
    font-size: 38px; font-weight: 700; color: var(--white); letter-spacing: 1px; line-height: 1;
  }
  .hero-accent {
    position: absolute; left: 77px; top: 134px;
    font-size: 52px; font-weight: 800; color: var(--gold); letter-spacing: 24px; line-height: 1;
  }
  .hero-cta {
    position: absolute; left: 76px; top: 217px; width: 232px; height: 46px;
    border: 3px solid var(--white); border-radius: 4px;
    background: linear-gradient(90deg, var(--gold-mid), var(--gold-light));
    color: var(--white); font-size: 16px; letter-spacing: 4px;
    display: flex; align-items: center; justify-content: center;
  }
  .about-title {
    position: absolute; left: 0; top: 538px; width: 1119px; text-align: center;
    font-size: 29px; font-weight: 700; color: var(--gold);
  }
  .about-sub {
    position: absolute; left: 0; top: 591px; width: 1119px; text-align: center;
    font-size: 15px; font-weight: 300; color: var(--gold); letter-spacing: 0.5px;
  }
  .timeline { position: absolute; left: 0; top: 0; }
  .step-num {
    font-family: "Montserrat", sans-serif; font-size: 14px; font-weight: 700; fill: var(--white);
  }
  .milestone {
    position: absolute; width: 428px;
    color: var(--white); font-size: 14.5px; letter-spacing: 2px; line-height: 26px;
    padding: 0 24px 0 27px; display: flex; flex-direction: column; justify-content: center;
  }
  .milestone .sub-point { font-size: 12px; padding-left: 34px; line-height: 22px; }
</style>
</head>
<body>
  <div class="fringe-band" role="img" aria-label="Decorative golden grass fringe along the top edge"></div>

  <header class="site-header">
    <div class="brand"><span class="brand-mark"></span>Halvorn Minerals</div>
    <nav class="main-nav">
      <a style="left:445px">Home</a>
      <a style="left:549px">About Us</a>
      <a style="left:684px">Projects</a>
      <a style="left:812px">Strategy</a>
      <a style="left:943px">Contact Us</a>
    </nav>
  </header>

  <section class="hero">
    <svg width="1119" height="349" viewBox="0 0 1119 349">
      <defs>
        <linearGradient id="cityTone" x1="0" y1="0" x2="1" y2="1">
          <stop offset="0" stop-color="#7d6c3c"/>
          <stop offset="0.5" stop-color="#a38b55"/>
          <stop offset="1" stop-color="#8a7546"/>
        </linearGradient>
      </defs>
      <rect width="1119" height="349" fill="var(--slate)"/>
      <polygon points="643,0 1119,0 1119,349 741,349" fill="var(--cream)"/>
      <polygon points="656,0 1119,0 1119,349 754,349" fill="url(#cityTone)" role="img" aria-label="Night skyline of a city tinted in gold"/>
    </svg>
    <h1 class="hero-title">SIGNIFICANT AMOUNT OF</h1>
    <div class="hero-accent">EXPERIENCE</div>
    <div class="hero-cta">contact us</div>
  </section>

  <h2 class="about-title">ABOUT US</h2>
  <div class="about-sub">from start</div>

  <svg class="timeline" width="1119" height="1200" viewBox="0 0 1119 1200">
    <line x1="560" y1="626" x2="560" y2="1200" stroke="var(--gold-mid)" stroke-width="3"/>
    <circle cx="560" cy="626" r="5" fill="var(--gold-mid)"/>
    <!-- left boxes -->
    <rect x="77" y="654" width="428" height="153" rx="4" fill="var(--slate)"/>
    <polygon points="505,758 519,770 505,782" fill="var(--slate)"/>
    <rect x="77" y="824" width="428" height="174" rx="4" fill="var(--slate)"/>
    <polygon points="505,919 519,931 505,943" fill="var(--slate)"/>
    <rect x="77" y="1015" width="428" height="200" rx="4" fill="var(--slate)"/>
    <polygon points="505,1077 519,1089 505,1101" fill="var(--slate)"/>
    <!-- right boxes -->
    <rect x="613" y="654" width="427" height="123" rx="4" fill="var(--slate)"/>
    <polygon points="613,672 599,684 613,696" fill="var(--slate)"/>
    <rect x="613" y="793" width="427" height="157" rx="4" fill="var(--slate)"/>
    <polygon points="613,831 599,843 613,855" fill="var(--slate)"/>
    <rect x="613" y="966" width="427" height="141" rx="4" fill="var(--slate)"/>
    <polygon points="613,993 599,1005 613,1017" fill="var(--slate)"/>
    <rect x="615" y="1124" width="427" height="100" rx="4" fill="var(--slate)"/>
    <polygon points="615,1148 601,1160 615,1172" fill="var(--slate)"/>
    <!-- steps -->
    <g fill="var(--gold-mid)" stroke="var(--cream)" stroke-width="2">
      <circle cx="560" cy="684" r="21"/><circle cx="560" cy="762" r="21"/>
      <circle cx="560" cy="843" r="21"/><circle cx="560" cy="924" r="21"/>
      <circle cx="560" cy="1005" r="21"/><circle cx="560" cy="1082" r="21"/>
      <circle cx="562" cy="1160" r="21"/>
    </g>
    <g class="step-num" text-anchor="middle">
      <text x="560" y="689">1</text><text x="560" y="767">2</text>
      <text x="560" y="848">3</text><text x="560" y="929">4</text>
      <text x="560" y="1010">5</text><text x="560" y="1087">6</text>
      <text x="562" y="1165">7</text>
    </g>
  </svg>

  <div class="milestone" style="left:77px;top:654px;height:153px">Strong executive &amp; management team with A to Z in all facets of mining, finance &amp; operations.</div>
  <div class="milestone" style="left:77px;top:824px;height:174px">On the ground experience with equipment &amp; personnel able to evaluate new projects &amp; acquire distressed assets.</div>
  <div class="milestone" style="left:77px;top:1028px;display:block">Project selectiocriteria based on delivering value uplift across the project development spectrum with a specific focus on the following economic outcomesn :<div class="sub-point">High NPV &amp; IRR;</div></div>
  <div class="milestone" style="left:613px;top:654px;height:123px">Newly formed company to create a platform for execution of global mining projects with an initial focus on South America, Central America &amp; Africa.</div>
  <div class="milestone" style="left:613px;top:793px;height:157px">Properly capitalized to execute its mandate.</div>
  <div class="milestone" style="left:613px;top:966px;height:141px">Previous experience in developing brownfield &amp; greenfield projects into producing assets.</div>
</body>
</html>
```